Website Design For Atelier Nine Design Group

Create a sophisticated website that denotes high-end luxury. We would like to keep the copy minimalist and elegantly understated while communicating only the most essential information. While creating an air of exclusivity.
We would like 3-4 Tab Wesbite
Home:
• Feature a design project front and centre, along with a short
introduction about who we are and what we do.

We can put a Call To Action at the end of the introduction inviting readers to learn more on our About page.
About:
• This page should provide more detail on our background, past
achievements, history of the company, and anything you'd like to
highlight.
• We should also provide details on our services, aesthetic, process, etc.
Team:
• introduce the team, possibly with short descriptions for each
team member. Total Team Members 7
Residential
• The portfolio page can be a grid of images along with titles for
each project.
• Clicking on each image should take you to a separate page for that
project where readers can find more details

Commercial
The portfolio page can be a grid of images along with titles for
each project.

Contact Us:

example website:
https://www.morvexinteriors.example/

Target Market(s)

High end luxury clientele

Industry/Entity Type

Interior Design

Number of Pages Required

4 page

Font styles to use
Sans Serif

Requirements
Must have
• Company logo, color scheme and name: Atelier Nine Design Group

```html
<!DOCTYPE html>
<html lang="en">
<head>
<meta charset="utf-8">
<title>Atelier Nine Design Group</title>
<link href="https://fonts.googleapis.com/css2?family=Questrial&display=swap" rel="stylesheet">
<style>
  :root {
    --ink: #1c1c1c;
    --muted: #666666;
    --white: #ffffff;
    --green: #10503f;
    --green-ink: #0f4a3b;
    --gold: #c49a2c;
    --rule: #8a8a8a;
    --form-rule: #cfd9d5;
  }
  * { box-sizing: border-box; margin: 0; padding: 0; }
  html, body { width: 1200px; height: 3264px; overflow: hidden; }
  body {
    position: relative;
    background: var(--white);
    color: var(--ink);
    font-family: "Questrial", sans-serif;
  }
  .abs { position: absolute; }

  /* Header */
  .site-header { left: 0; top: 0; width: 1200px; height: 91px; border-bottom: 1px solid #d4d4d4; }
  .brand { left: 91px; top: 34px; display: flex; align-items: center; gap: 10px;
    font-size: 20px; letter-spacing: 0.12em; color: var(--ink); }
  .brand-square { width: 14px; height: 14px; border: 2px solid var(--ink); }
  .main-nav a { position: absolute; top: 42px; font-size: 13px; color: var(--ink);
    text-decoration: none; letter-spacing: 0.02em; }
  .main-nav a.is-current { color: #8c8c8c; }

  /* Hero */
  .hero { left: 0; top: 91px; width: 1200px; height: 619px; }
  .hero-panel { position: absolute; top: 0; height: 619px; }
  .hero-bath { left: 0; width: 414px; background: linear-gradient(160deg, #a4a4a6, #76777a 60%, #8e8f92); }
  .hero-living { left: 414px; width: 415px; background: linear-gradient(170deg, #3f5a4d, #8d8a84 45%, #b8b4ad); }
  .hero-study { left: 829px; width: 371px; background: linear-gradient(170deg, #3b4143, #6a6e6e 50%, #9a9c9d); }
  .hero-title { left: 381px; top: 460px; color: var(--white); font-size: 32px;
    letter-spacing: 0.13em; line-height: 39px; }

  /* Intro */
  .intro { left: 508px; top: 770px; width: 640px; font-size: 42px; line-height: 56px; color: var(--ink); }

  /* About */
  .about-title { left: 23px; top: 1138px; font-size: 30px; letter-spacing: 0.32em; }
  .about-copy { left: 22px; top: 1218px; width: 370px; font-size: 15px; line-height: 25.6px; }
  .about-link { left: 22px; top: 1503px; font-size: 15px; color: var(--gold);
    text-decoration: underline; display: flex; align-items: center; gap: 10px; }
  .about-image { left: 499px; top: 1068px; width: 701px; height: 625px;
    background: linear-gradient(165deg, #d8d8d6, #ecebe8 40%, #a7a199 75%, #cfcac3); }

  /* Stats */
  .stat-rule { left: 281px; width: 701px; height: 1px; background: var(--rule); }
  .stat { left: 352px; display: flex; align-items: baseline; gap: 24px; }
  .stat-number { font-size: 62px; color: var(--green-ink); }
  .stat-label { font-size: 30px; color: var(--ink); }

  /* Projects */
  .project-card { top: 2283px; width: 373px; height: 439px; }
  .project-bath { left: 22px; background: linear-gradient(165deg, #8d8d8f, #bdbdbf 55%, #7b7b7d); }
  .project-study { left: 416px; background: linear-gradient(170deg, #3f4446, #7b7a76 55%, #a9a6a0); }
  .project-living { left: 810px; background: linear-gradient(170deg, #3d584b, #9b968e 50%, #c3bfb8); }
  .project-caption { position: absolute; left: 16px; right: 16px; bottom: 24px;
    display: flex; justify-content: space-between; align-items: baseline;
    color: var(--white); font-size: 15px; }
  .project-caption .view { font-size: 11px; }

  /* Contact */
  .contact-band { left: 0; top: 2823px; width: 1200px; height: 376px; background: var(--green); }
  .contact-lead { left: 66px; top: 2905px; width: 340px; font-size: 32px; line-height: 38px; color: var(--white); }
  .field-label { left: 615px; font-size: 12px; color: var(--white); }
  .field-rule { left: 615px; width: 501px; height: 1px; background: var(--form-rule); }
  .submit-button { left: 615px; top: 3112px; width: 120px; height: 43px; border: 1px solid var(--white);
    color: var(--white); font-size: 15px; display: flex; align-items: center; justify-content: center; }

  /* Footer */
  .site-footer { left: 0; top: 3199px; width: 1200px; height: 65px; font-size: 14px; }
  .footer-item { position: absolute; top: 27px; }
  .footer-copy { left: 66px; font-size: 12px; top: 29px; }
  .social-dot { position: absolute; top: 27px; width: 18px; height: 18px; border: 2px solid var(--ink); border-radius: 50%; }
</style>
</head>
<body>

<header class="site-header abs">
  <div class="brand abs"><span class="brand-square"></span><span>ATELIER NINE</span></div>
  <nav class="main-nav">
    <a href="#" style="left:587px">HOME</a>
    <a href="#" class="is-current" style="left:707px">ABOUT</a>
    <a href="#" style="left:825px">COMMERCIAL</a>
    <a href="#" style="left:986px">CONTACT US</a>
  </nav>
</header>

<section class="hero abs">
  <div class="hero-panel hero-bath" role="img" aria-label="Marble bathroom with freestanding bathtub and wooden side stool"></div>
  <div class="hero-panel hero-living" role="img" aria-label="Living room with green walls, patterned curtains and woven pendant light"></div>
  <div class="hero-panel hero-study" role="img" aria-label="Study with built-in shelving, desk and upholstered chair"></div>
</section>
<h1 class="hero-title abs">INTERIOR DESIGN COMPANY:<br>QUALITY &amp; LUXURY DESIGN</h1>

<p class="intro abs">Atelier Nine is an interior design firm focused on creating great and luxurious places to better life</p>

<h2 class="about-title abs">ABOUT US</h2>
<p class="about-copy abs">Lorem ipsum dolor sit amet, consectetur adipiscing elit. Vitae risus gravida porta amet in scelerisque in amet phasellus. Leo egestas dignissim et elit at dolor. Iaculis eget libero morbi velit at. Est magna leo dui, mattis mauris integer. Quis elementum sit tristique pellentesque orci venenatis, at facilisi. Amet at massa mattis in dictum orci facilisis sed condimentum. Est curabitur eget erat ac diam donec et, diam.</p>
<a class="about-link abs" href="#">MORE ABOUT US
  <svg width="14" height="12" viewBox="0 0 14 12" aria-hidden="true"><path d="M1 6h11M7 1l5 5-5 5" fill="none" stroke="#c49a2c" stroke-width="1.4"/></svg>
</a>
<div class="about-image abs" role="img" aria-label="Bright living room with sectional sofa, round coffee table and slatted wall"></div>

<div class="stat abs" style="top:1880px"><span class="stat-number">38</span><span class="stat-label">AWESOME PROJECTS</span></div>
<div class="stat-rule abs" style="top:1958px"></div>
<div class="stat abs" style="top:1966px"><span class="stat-number">20</span><span class="stat-label">HAPPY CLIENTS</span></div>
<div class="stat-rule abs" style="top:2058px"></div>
<div class="stat abs" style="top:2073px"><span class="stat-number">38</span><span class="stat-label">PROJECT FINISHED</span></div>

<article class="project-card project-bath abs" role="img" aria-label="Project photo: marble bathroom with freestanding tub">
  <div class="project-caption"><span>House of Mr. Hallam</span><span class="view">VIEW</span></div>
</article>
<article class="project-card project-study abs" role="img" aria-label="Project photo: study with shelving and desk">
  <div class="project-caption"><span>House of Mr. Hallam</span><span class="view">VIEW</span></div>
</article>
<article class="project-card project-living abs" role="img" aria-label="Project photo: living room with curtains and pendant light">
  <div class="project-caption"><span>House of Mr. Hallam</span><span class="view">VIEW</span></div>
</article>

<section class="contact-band abs"></section>
<p class="contact-lead abs">Don’t hesitate to contact us and we’ll create a piece of art of you</p>
<span class="field-label abs" style="top:2895px">Your Name</span>
<div class="field-rule abs" style="top:2919px"></div>
<span class="field-label abs" style="top:2931px">Your Phone</span>
<div class="field-rule abs" style="top:2956px"></div>
<span class="field-label abs" style="top:2963px">Your Email</span>
<div class="field-rule abs" style="top:2988px"></div>
<span class="field-label abs" style="top:3000px">Message</span>
<div class="field-rule abs" style="top:3063px"></div>
<div class="submit-button abs">Submit</div>

<footer class="site-footer abs">
  <span class="footer-item footer-copy">© Atelier Nine All Rights Reserved</span>
  <span class="footer-item" style="left:530px">555 014 2290</span>
  <span class="footer-item" style="left:703px">enquiry@ateliernine.example</span>
  <span class="social-dot" style="left:1070px" aria-label="Social profile"></span>
  <span class="social-dot" style="left:1110px" aria-label="Social profile"></span>
</footer>

</body>
</html>
```